standardize print collateral

we need help standardizing all print collateral and website. top priorities:

1. standardized case studies template
2. standardized marketing slicks template
3. standardized powerpoint template
Updates

Project Deadline Extended
Reason: We are extending the project to allow current design submissions to be tweaked while providing the opportunity for new designs to be submitted. We will need all 3 collateral designs submitted to make a final decision. Please note, these 3 designs should all look different, needless to say they should all compliment eachother. As for some direction, the powerpoint main color should not be yellow since yellow does not show up the same shade on any screen. The case study and marketing slicks will be printed and often sit next to our competitors marketing material - think high end product, technology, revolutionary, edgy, professional. The designs should compliment eachother and feel like the Brightfen Metrics brand (which you are determining) and should stand out professionally. We are open to introducing new colors into our brand, the only thing that must remain the same is our logo. Have fun, make it edgy, and keep it professional. Looking forward to seeing what you submit!

Target Market(s)

Property Casualty Insurance Companies: Executive level wording with actuarial credibility

Industry/Entity Type

Marketing

Requirements
Must have
• professional layout for existing collateral and 2-page marketing slicks. style guide/colors can be transferred to powerpoint. logo must stay; everything else (i.e. color, font, layout/structure etc.) is flexible. The three components should not looks the same, they should only compliment eachother.
Nice to have
• we are revolutionizing a conservative industry, so adequate level of edgy/advanced technology/impactful feel to layout
Should not have
• no need to stay within color constraints of yellow, but need to appropriately work well with the eagle head logo

```html
<!DOCTYPE html>
<html lang="en">
<head>
<meta charset="utf-8">
<title>Rapid Portfolio Analysis – Brightfen Metrics</title>
<link href="https://fonts.googleapis.com/css2?family=Barlow:wght@400;500;600;700&display=swap" rel="stylesheet">
<style>
:root{
  --gold:#e6b02b;
  --ink:#1c1c1c;
  --grey:#6e6e6e;
  --panel:#e6e6e6;
  --paper:#ffffff;
  --backdrop:#ebe8e3;
}
*{box-sizing:border-box;margin:0;padding:0}
html,body{width:1200px;height:832px;overflow:hidden}
body{background:var(--backdrop);font-family:"Barlow",Arial,sans-serif;color:var(--ink);position:relative}
.sheet{position:absolute;top:50px;width:540px;height:766px;background:var(--paper);overflow:hidden}
.sheet--front{left:48px}
.sheet--back{left:612px}
.abs{position:absolute}
.header-band{position:absolute;left:0;top:0;width:540px;height:190px}
.eagle-art{position:absolute;background:linear-gradient(135deg,#d8d8d8,#8d8d8d 60%,#4a4a4a);border-radius:60% 40% 50% 50% / 55% 45% 55% 45%;opacity:.9}
.title{left:20px;top:40px;font-size:28px;line-height:1;font-weight:500;color:#fff;letter-spacing:.5px}
.title strong{display:block;color:var(--ink);font-weight:700}
.tagline{left:72px;top:122px;font-size:16px;line-height:1.05;font-weight:500;color:var(--ink)}
.tagline span{display:block;color:var(--gold);font-weight:700}
.brand-name{font-weight:500;color:#333;letter-spacing:.2px;line-height:1}
.body-copy{font-size:9.3px;line-height:1.25;text-align:justify;color:#2a2a2a}
.how-tab{left:18px;top:270px;width:200px;height:24px;background:var(--ink);color:#fff;font-size:17px;line-height:24px;padding-left:10px;font-weight:500}
.how-box{left:18px;top:294px;width:504px;height:184px;background:var(--gold);display:flex;padding:8px 4px}
.how-col{flex:1;padding:0 7px;border-right:1px dotted rgba(255,255,255,.8);color:#fff}
.how-col:last-child{border-right:none}
.how-col h3{font-size:10.5px;font-weight:700;line-height:1.1}
.how-col h4{font-size:11.5px;font-weight:700;color:var(--ink);line-height:1.1;margin-bottom:5px}
.how-col p{font-size:9px;line-height:1.22}
.mini-title{font-size:10px;font-weight:700;color:var(--ink)}
.mini-caption{font-size:8.6px;line-height:1.2;color:var(--gold)}
.section-head{left:36px;top:604px;font-size:13.5px;line-height:1.15;font-weight:700;color:#444}
.chart-title{font-size:11px;font-weight:700;color:var(--ink)}
.chart-caption{font-size:9.6px;line-height:1.25;color:#555}
.lead{left:52px;top:186px;width:440px;font-size:13px;line-height:1.2;font-weight:700;color:#555}
.rule-dotted{left:0;width:540px;border-top:2px dotted var(--gold)}
.grey-panel{left:16px;top:412px;width:508px;height:170px;background:var(--panel)}
.closing{left:52px;top:592px;width:440px;font-size:13px;line-height:1.2;font-weight:700;color:#555}
.about{left:20px;top:716px;width:240px;font-size:8.2px;line-height:1.25;color:#333}
.about b{font-weight:700}
.address{right:24px;top:690px;text-align:right;font-size:9.4px;line-height:1.3;color:#333;font-style:normal}
.address .web{font-weight:700;letter-spacing:2px;margin-top:3px;display:block}
.address .sep{color:var(--gold)}
svg text{font-family:"Barlow",Arial,sans-serif}
</style>
</head>
<body>

<section class="sheet sheet--front">
  <svg class="header-band" viewBox="0 0 540 190" aria-hidden="true">
    <defs>
      <linearGradient id="bandFront" x1="0" x2="1" y1="0" y2="0">
        <stop offset="0" stop-color="#e6b02b"/>
        <stop offset=".55" stop-color="#a78534"/>
        <stop offset="1" stop-color="#2c2c2c"/>
      </linearGradient>
    </defs>
    <rect width="540" height="190" fill="#1c1c1c"/>
    <path d="M0 34 C180 34 360 26 540 8 L540 190 L0 190Z" fill="url(#bandFront)"/>
    <path d="M0 112 C200 112 380 96 540 52 L540 190 L0 190Z" fill="#fff"/>
    <path d="M0 112 C200 112 380 96 540 52" fill="none" stroke="#cfcfcf" stroke-width="1.5"/>
  </svg>
  <h1 class="abs title">RAPID PORTFOLIO<strong>ANALYSIS</strong></h1>
  <div class="abs eagle-art" style="left:380px;top:50px;width:150px;height:100px" role="img" aria-label="Grey eagle head illustration"></div>
  <h2 class="abs tagline">WINNING AGAINSY<span>ADVERSE SELECTION</span></h2>
  <div class="abs brand-name" style="left:300px;top:152px;font-size:24px">Brightfen Metrics</div>

  <p class="abs body-copy" style="left:24px;top:186px;width:492px">The property and casualty market is over-supplied with excess capacity, and current pricing methods are inconsistent and outdated. This leads to a considerable level of adverse selection within nearly every portfolio. Almost every insurer is attracting customers who are underpriced and losing business where they are overpriced. This invisible effect only surfaces after evidence of slowly deteriorating portfolio loss ratios, resulting in premium increases across the portfolio. These across-the-board premium increases exacerbate the problem by overpricing the most profitable customers and driving them into the arms of competitors.</p>

  <div class="abs how-tab">HOW DOES IT WORK?</div>
  <div class="abs how-box">
    <div class="how-col">
      <h3>DETECTION</h3>
      <h4>Is the portfolio priced correctly?</h4>
      <p>Kestrel employs a regression method based on a technological breakthrough. It exposes pricing imbalances by commonly employed rating method including the GLM. These pricing imbalances are the major drivers of adverse selection.</p>
    </div>
    <div class="how-col">
      <h3>MEASUREMENT</h3>
      <h4>How is the portfolio trending?</h4>
      <p>Kestrel scores the two most important attributes of the portfolio: the adequacy of rates and the quality of the business on a progressive basis. In addition, Kestrel projects the financial outcome of business as it is written with startling accuracy. Insurers are able to know significantly in advance of trends in their business.</p>
    </div>
    <div class="how-col">
      <h3>CORRECTION</h3>
      <h4>How to address the issues?</h4>
      <p>Kestrel provides an array of options for addressing any deterioration in the portfolio. These options range from specifically designed rate adjustments and underwriting strategies, to simple distribution management sales and profitability strategies.</p>
    </div>
  </div>

  <div class="abs mini-title" style="left:40px;top:484px">Portfolio Monitoring</div>
  <svg class="abs" style="left:40px;top:497px" width="232" height="64" viewBox="0 0 232 74" preserveAspectRatio="none" aria-label="Portfolio monitoring table">
    <rect width="232" height="74" fill="#fff" stroke="#bbb" stroke-width=".5"/>
    <rect width="232" height="11" fill="#eee"/>
    <g font-size="5.5" fill="#333"><text x="3" y="8">Year</text><text x="40" y="8">Earned</text><text x="80" y="8">Written</text><text x="120" y="8">Claims</text><text x="160" y="8">Loss</text><text x="196" y="8">Score</text></g>
    <g stroke="#999" stroke-width="1.4">
      <path d="M3 17h28M40 17h30M80 17h30M120 17h24M160 17h20M196 17h22"/>
      <path d="M3 24h28M40 24h30M80 24h30M120 24h24M160 24h20M196 24h22"/>
      <path d="M3 31h28M40 31h30M80 31h30M120 31h24M160 31h20M196 31h22"/>
      <path d="M3 38h28M40 38h30M80 38h30M120 38h24M160 38h20M196 38h22"/>
      <path d="M3 45h28M40 45h30M80 45h30M120 45h24M160 45h20M196 45h22"/>
      <path d="M3 52h28M40 52h30M80 52h30M120 52h24M160 52h20M196 52h22"/>
      <path d="M3 59h28M40 59h30M80 59h30M120 59h24M160 59h20M196 59h22"/>
      <path d="M3 66h28M40 66h30M80 66h30M120 66h24M160 66h20M196 66h22"/>
    </g>
    <g opacity=".75"><rect x="180" y="13" width="12" height="5" fill="#e55"/><rect x="180" y="27" width="12" height="5" fill="#6b6"/><rect x="180" y="41" width="12" height="5" fill="#ec5"/><rect x="180" y="55" width="12" height="5" fill="#6b6"/><rect x="180" y="62" width="12" height="5" fill="#e55"/></g>
  </svg>
  <p class="abs mini-caption" style="left:40px;top:565px;width:230px">Predict the future loss ratio of the business being written - both renewals and new business.</p>

  <div class="abs mini-title" style="left:294px;top:484px">Distribution Monitoring</div>
  <svg class="abs" style="left:294px;top:497px" width="214" height="68" viewBox="0 0 214 80" preserveAspectRatio="none" aria-label="Distribution monitoring heat map">
    <rect width="214" height="80" fill="#fff" stroke="#bbb" stroke-width=".5"/>
    <rect width="214" height="8" fill="#cfd9c8"/>
    <rect x="40" y="10" width="40" height="68" fill="#3d8a3d"/>
    <rect x="40" y="30" width="40" height="14" fill="#e7c84a"/>
    <rect x="40" y="58" width="40" height="20" fill="#c9463d"/>
    <rect x="84" y="10" width="50" height="68" fill="#5fa55a"/>
    <rect x="84" y="20" width="50" height="10" fill="#e7c84a"/>
    <rect x="84" y="48" width="50" height="30" fill="#c9463d"/>
    <rect x="138" y="10" width="36" height="68" fill="#4c994a"/>
    <rect x="138" y="40" width="36" height="12" fill="#e7c84a"/>
    <rect x="138" y="64" width="36" height="14" fill="#d0523d"/>
    <rect x="178" y="10" width="32" height="68" fill="#7fb86a"/>
    <rect x="178" y="52" width="32" height="26" fill="#e0a84a"/>
    <g stroke="#fff" stroke-width=".6"><path d="M0 17h214M0 24h214M0 31h214M0 38h214M0 45h214M0 52h214M0 59h214M0 66h214M0 73h214"/></g>
    <g stroke="#999" stroke-width="1.2"><path d="M4 14h30M4 21h30M4 28h30M4 35h30M4 42h30M4 49h30M4 56h30M4 63h30M4 70h30"/></g>
  </svg>
  <p class="abs mini-caption" style="left:294px;top:569px;width:220px">Constantly track the quality and performance of individual distribution outlets based on the underwriting score of each policy</p>

  <h2 class="abs section-head">LET BRIGHTFEN METRICS BUILD<br>YOUR PORTFOLIO ANALYSIS REPORT</h2>
  <p class="abs body-copy" style="left:36px;top:641px;width:480px">The report details your portfolio trends and identifies future unseen problems before they occur. The insight provided in the report exhibits what is actually going on in your portfolio. This likely includes adverse selection, impact of price changes with unintended consequences, and the emerging trends in the composition of the book. The analysis results not only reveal past trends, but also predict future impact.</p>

  <svg class="abs" style="left:0;top:722px" width="540" height="44" viewBox="0 0 540 44" aria-hidden="true">
    <path d="M0 30 C180 10 360 4 540 14 L540 44 L0 44Z" fill="#d6d6d6"/>
    <path d="M0 38 C200 24 380 20 540 26 L540 44 L0 44Z" fill="#b9b9b9"/>
  </svg>
</section>

<section class="sheet sheet--back">
  <svg class="header-band" viewBox="0 0 540 190" aria-hidden="true">
    <defs>
      <linearGradient id="bandBack" x1="0" x2="1" y1="0" y2="0">
        <stop offset="0" stop-color="#e6b02b"/>
        <stop offset=".5" stop-color="#9f8038"/>
        <stop offset="1" stop-color="#262626"/>
      </linearGradient>
    </defs>
    <rect width="540" height="190" fill="#1c1c1c"/>
    <path d="M0 30 C200 26 360 22 540 8 L540 190 L0 190Z" fill="url(#bandBack)"/>
    <path d="M0 150 C160 140 360 60 540 40 L540 190 L0 190Z" fill="#fff"/>
    <path d="M0 150 C160 140 360 60 540 40" fill="none" stroke="#cfcfcf" stroke-width="1.5"/>
  </svg>
  <div class="abs rule-dotted" style="top:226px"></div>
  <h2 class="abs lead">Kestrel detects, measures and presents actionable options to correct the insurance company effects of adverse selection within any P&amp;C portfolio.</h2>

  <div class="abs chart-title" style="left:56px;top:240px">Underwriting Score</div>
  <svg class="abs" style="left:48px;top:254px" width="226" height="118" viewBox="0 0 226 118" aria-label="Underwriting score bar chart">
    <g font-size="5.5" fill="#555">
      <text x="4" y="12">80%</text><text x="4" y="32">60%</text><text x="4" y="52">40%</text><text x="4" y="72">20%</text><text x="6" y="92">0%</text>
    </g>
    <path d="M22 90H222M22 10V90" stroke="#999" stroke-width=".6"/>
    <g fill="#e6b02b">
      <rect x="30" y="23" width="16" height="67"/>
      <rect x="62" y="44" width="16" height="46"/>
      <rect x="94" y="61" width="16" height="29"/>
      <rect x="126" y="64" width="16" height="26"/>
      <rect x="158" y="69" width="16" height="21"/>
      <rect x="190" y="74" width="16" height="16"/>
    </g>
    <g font-size="5" fill="#555" text-anchor="middle">
      <text x="38" y="98">0-50</text><text x="70" y="98">50-249</text><text x="102" y="98">250-499</text><text x="134" y="98">500-749</text><text x="166" y="98">750-899</text><text x="198" y="98">900-1000</text>
      <text x="122" y="108">Score Tier</text>
    </g>
  </svg>
  <p class="abs chart-caption" style="left:56px;top:372px;width:210px">Discover the pricing imbalances within the portfolio. These imbalances are the main driver of the adverse selection.</p>

  <div class="abs" style="left:282px;top:236px;height:136px;border-left:1px dotted #bbb"></div>
  <div class="abs chart-title" style="left:318px;top:240px">Trend and loss ratio</div>
  <svg class="abs" style="left:296px;top:254px" width="216" height="118" viewBox="0 0 216 118" aria-label="Trend and loss ratio bubble chart">
    <path d="M100 6V90M12 90H210" stroke="#999" stroke-width=".6"/>
    <path d="M12 48H196" stroke="#5a7bbf" stroke-width="1"/>
    <text x="198" y="50" font-size="6" fill="#333">40%</text>
    <g fill="#c9d6ee" stroke="#8ea6d8" stroke-width=".8">
      <circle cx="170" cy="34" r="10"/><circle cx="80" cy="42" r="8"/><circle cx="70" cy="58" r="8"/><circle cx="58" cy="72" r="9"/>
    </g>
    <g font-size="6" fill="#333" text-anchor="middle"><text x="170" y="36">1</text><text x="80" y="44">3</text><text x="70" y="60">4</text><text x="58" y="74">2</text></g>
    <g font-size="5" fill="#555" text-anchor="middle"><text x="14" y="98">-40%</text><text x="56" y="98">-20%</text><text x="100" y="98">0%</text><text x="144" y="98">20%</text><text x="188" y="98">40%</text><text x="100" y="108">Growth/Decline</text></g>
    <text x="6" y="52" font-size="5" fill="#555" transform="rotate(-90 6 52)">Loss Ratio</text>
  </svg>
  <p class="abs chart-caption" style="left:318px;top:372px;width:200px">Show trends within the portfolio in real time covering premium adequacy and the quality of all business being written.</p>

  <div class="abs grey-panel"></div>
  <p class="abs chart-caption" style="left:56px;top:420px;width:440px">Report on detailed analyses including sales trend and profitability trends. This allows for a method of managing distribution channels while addressing pricing imbalances.</p>

  <div class="abs chart-title" style="left:60px;top:458px">Portfolio exposure</div>
  <svg class="abs" style="left:50px;top:472px" width="210" height="104" viewBox="0 0 210 104" aria-label="Portfolio exposure line chart">
    <path d="M24 6V78H206" stroke="#999" stroke-width=".6" fill="none"/>
    <g stroke="#fff" stroke-width=".6"><path d="M24 18H206M24 30H206M24 42H206M24 54H206M24 66H206"/></g>
    <g font-size="5" fill="#555"><text x="6" y="9">550</text><text x="6" y="21">530</text><text x="6" y="33">510</text><text x="6" y="45">490</text><text x="6" y="57">470</text><text x="6" y="69">450</text></g>
    <path d="M28 30 L38 24 L46 30 L54 22 L62 28 L70 20 L78 26 L86 18 L94 24 L102 20 L110 26 L118 24 L126 30 L132 28 L140 44 L148 52 L156 48 L164 56 L172 52 L180 60 L188 56 L196 64 L204 68" fill="none" stroke="#e6b02b" stroke-width="1.8"/>
    <g font-size="4.5" fill="#555"><text x="28" y="96" transform="rotate(-90 28 96)">01/2010</text><text x="60" y="96" transform="rotate(-90 60 96)">01/2011</text><text x="92" y="96" transform="rotate(-90 92 96)">01/2012</text><text x="124" y="96" transform="rotate(-90 124 96)">01/2013</text><text x="156" y="96" transform="rotate(-90 156 96)">01/2014</text><text x="188" y="96" transform="rotate(-90 188 96)">01/2015</text></g>
  </svg>

  <div class="abs chart-title" style="left:312px;top:458px">Premium Change</div>
  <svg class="abs" style="left:300px;top:472px" width="200" height="104" viewBox="0 0 200 104" aria-label="Premium change bar chart">
    <path d="M22 4V96M22 40H196" stroke="#999" stroke-width=".6"/>
    <g font-size="5" fill="#555"><text x="4" y="8">60%</text><text x="4" y="24">30%</text><text x="6" y="42">0%</text><text x="2" y="60">-30%</text><text x="2" y="78">-60%</text></g>
    <g fill="#e6b02b">
      <rect x="34" y="40" width="16" height="4"/>
      <rect x="76" y="40" width="16" height="40"/>
      <rect x="118" y="14" width="16" height="26"/>
      <rect x="160" y="26" width="16" height="14"/>
    </g>
    <g font-size="5.5" fill="#333" text-anchor="middle"><text x="42" y="50">1</text><text x="84" y="52">2</text><text x="126" y="46">3</text><text x="168" y="46">4</text><text x="108" y="96">Segment Number</text></g>
  </svg>

  <p class="abs closing">Through the use of these advanced analytics your company has the opportunity to future proof each of your portfolios.</p>

  <svg class="abs" style="left:0;top:626px" width="540" height="140" viewBox="0 0 540 140" aria-hidden="true">
    <path d="M0 40 C200 20 400 30 540 60 L540 140 L0 140Z" fill="#e4e4e4"/>
    <path d="M0 100 C220 80 400 70 540 84 L540 140 L0 140Z" fill="#d2d2d2"/>
  </svg>
  <div class="abs eagle-art" style="left:50px;top:636px;width:90px;height:54px" role="img" aria-label="Grey eagle head illustration"></div>
  <div class="abs brand-name" style="left:22px;top:696px;font-size:17px">Brightfen Metrics</div>
  <p class="abs about"><b>Brightfen Metrics</b> provides breakthrough predictive analytics powered by machine learning and the latest statistical techniques, enabling property and casualty insurers to achieve superior performance.</p>
  <address class="abs address">Brightfen Metrics, 118 Larkmoor Avenue,<br>Suite 40, Ashbury, SC 29000<br>Phone: 555.014.2290 <span class="sep">|</span> Fax: 555.014.2291<span class="web">www.brightfenmetrics.com</span></address>
</section>

</body>
</html>
```